Flyer für Onlineshop
Zielgruppe
Wir vertreiben 2 Komponentenlacke, wasserbasiert, auf Polyurethanharz Basis zur Sanierung von Fliesen vieles und mehr.
Aufgabenstellung
Wir möchten eine Fleyer speziell für die Fliesenfarben.
Das Design soll frisch, modern und ansprechend gestaltet sein. Wir möchten den Fleyer öffentlich auslegen aber auch an z.B Jugendherbergen, Kurhäuser ect. und privat Personen verteilen um darauf aufmerksam zu machen das es eine güstige alternative zum Neukauf gibt.
Auf dem Flyer soll in der Fliesenlack im Vordergrund stehen es darf aber kurz auf weitere Produkte aufmerksam gemacht werden.
für die Größe des Flyers habe ich keine genauen Vorstellungen lasse mich überraschen.
Sie finden die Informationen die Sie benötigen unter
www.ralbo-sonderlacke.com/farben-lacke/fliesenfarbe
Der Fleyer sollte die Maße DIN lang (105 x 210 mm) hoch / 4 Seiten
Aber auch andere Vorschläge sind Willkommen
Also Logo habe ich verschiedene jpg´s hochgeladen..leider ist die qualität nicht sehr gut aber vielleicht können Sie was damit anfangen.
Bei weiteren Fragen stehe ich Ihnen gerne zur Verfügung

```html
<!DOCTYPE html>
<html lang="de">
<head>
<meta charset="utf-8">
<title>Die Fliesenfarbe – Flyer</title>
<link href="https://fonts.googleapis.com/css2?family=Oswald:wght@300;400&family=Source+Sans+3:wght@400;700&display=swap" rel="stylesheet">
<style>
  :root {
    --blue: #1f6fe5;
    --ink: #1e1e1e;
    --panel: #cfdcdc;
    --paper: #ffffff;
    --bg: #ffffff;
    --photo-bath: linear-gradient(135deg, #e9eef0, #c9d2d6 60%, #8f8f8f);
    --photo-roll: linear-gradient(90deg, #6f9a9a 0%, #8fb3b1 44%, #eef2f2 46%, #f7f9f9 100%);
    --photo-tiles: linear-gradient(135deg, #7a1a1a, #d8402a 35%, #f0a020 60%, #5a8a20 85%, #2a3a70);
  }
  * { box-sizing: border-box; margin: 0; padding: 0; }
  html, body { width: 848px; height: 1200px; overflow: hidden; background: var(--bg); }
  body { position: relative; font-family: "Source Sans 3", sans-serif; color: var(--ink); }
  .sheet { position: absolute; left: 10px; top: 162px; width: 828px; height: 874px; background: var(--paper); }
  .abs { position: absolute; }
  .tab { left: 35px; top: 163px; width: 26px; height: 40px; background: var(--blue); }
  .title { left: 51px; top: 218px; font-family: "Oswald", sans-serif; font-weight: 300; font-size: 45px; letter-spacing: 3px; line-height: 1; color: var(--ink); }
  .title .initial { color: var(--blue); }
  .subtitle { left: 52px; top: 264px; font-size: 13.6px; font-weight: 700; }
  .copy { font-size: 13.4px; line-height: 21.9px; text-align: justify; }
  .copy b { font-weight: 700; }
  .intro { left: 52px; top: 308px; width: 354px; }
  .body-text { left: 51px; top: 686px; width: 355px; }
  .photo { position: absolute; }
  .photo .strip { position: absolute; top: 0; bottom: 0; width: 24px; background: var(--blue); }
  .photo-bath { left: 35px; top: 480px; width: 369px; height: 191px; background: var(--photo-bath); }
  .photo-bath .strip { left: 0; }
  .panel { left: 438px; top: 203px; width: 383px; height: 809px; background: var(--panel); }
  .photo-roll { left: 458px; top: 226px; width: 342px; height: 192px; background: var(--photo-roll); }
  .photo-tiles { left: 458px; top: 798px; width: 342px; height: 192px; background: var(--photo-tiles); }
  .photo-roll .strip, .photo-tiles .strip { right: 0; }
  .panel-heading { left: 460px; top: 428px; font-family: "Oswald", sans-serif; font-weight: 400; font-size: 27px; letter-spacing: 1.6px; color: var(--blue); transform: scaleX(0.78); transform-origin: left; white-space: nowrap; }
  .panel-sub { left: 461px; top: 464px; font-size: 13.6px; font-weight: 700; }
  .list-mark { left: 460px; top: 500px; width: 25px; height: 60px; background: var(--blue); }
  .finish-list { left: 497px; top: 498px; list-style: none; font-size: 13.4px; line-height: 20.6px; }
  .details { left: 460px; top: 579px; width: 337px; line-height: 20.6px; }
</style>
</head>
<body>
  <div class="sheet"></div>
  <div class="abs tab"></div>
  <h1 class="abs title"><span class="initial">D</span>IE FLIESENFARBE</h1>
  <p class="abs subtitle">Ihres Bades oder Ihrer Küche gefällt Ihnen nicht mehr?</p>
  <p class="abs copy intro">Das ist kein Grund zum Verzagen, denn mit dem Fliesenlack aus dem <b>Ralbo-Sonderlacke-Sortiment</b>, kann Ihr Bad und Ihre Küche schon bald <b>in Ihrer Lieblingsfarbe</b> erstrahlen. Verzichten Sie darauf, die in die Jahre gekommenen Fliesen <b>abzuschlagen</b> und anschließend <b>neue Fliesen verlegen</b> zu lassen! So eine <b>Renovierung kostet</b> nicht nur sehr viel Geld, sie verursacht auch viel <b>Staub und Lärm</b>.</p>

  <div class="photo photo-bath" role="img" aria-label="Helles, modernes Badezimmer mit Badewanne und Glasdusche"><span class="strip"></span></div>

  <p class="abs copy body-text">Ob in <b>Bad</b>, <b>Küche</b> oder <b>Lagerraum</b>, Fliesen haben ohne Zweifel einen hohen praktischen Nutzen. Direkt nach dem Kauf findet man sie meist sehr schön. <b>Mit der Zeit jedoch verblasst oft ihr Glanz oder ihr Design kommt aus der Mode.</b> Es ist nicht unüblich, dass sich der persönliche Geschmack mit den Jahren wandelt. Wer Ralbo Fliesenfarbe verwendet, begegnet diesem Umstand, <b>ohne eine aufwändige Sanierung</b> mit teuren neuen Fliesen vornehmen zu müssen. <b>Lärm, Staub</b> und <b>Schmutz</b> durch einen Fliesenwechsel <b>müssen nicht sein</b>, denn unsere Fliesenlacke <b>haften und decken sehr gut, wobei sie wasserverdünnbar auf der Basis einer Kunststoffdispersion</b> sind. Gegen <b>Licht, Wetter und Chemikalien bestehen die Spezialfarben ebenfalls.</b> Je nach Variante bleibt der Farbton dabei <b>matt</b> oder <b>glänzt</b> ansprechend.</p>

  <div class="abs panel"></div>
  <div class="photo photo-roll" role="img" aria-label="Hand streicht Fliesen mit einer Farbrolle, vorher und nachher"><span class="strip"></span></div>
  <h2 class="abs panel-heading">GEBRAUCHSFERTIGE FLIESENFARBEN</h2>
  <p class="abs panel-sub">in vielen schönen Farbvariationen</p>
  <div class="abs list-mark"></div>
  <ul class="abs finish-list">
    <li>seidenglänzend für ein apartes Badezimmer</li>
    <li>matt für Keller oder Garage</li>
    <li>hochglänzend für Bad oder Küche</li>
  </ul>
  <p class="abs copy details">Dabei stehen <b>zahlreiche Farbtöne</b> zur Auswahl, damit für jeden Möbelstil und jeden Geschmack das Passende gefunden werden kann. Neben <b>helleren und dunkleren</b> Varianten sind <b>kalte und warme Töne</b> verfügbar. Bevor der Decklack aufgetragen werden kann, sind eine reinigende Vorbehandlung, das Trocknen und der Auftrag der Grundierung nötig. Die dafür nötigen Produkte lassen sich separat <b>in unserem Onlineshop</b> erwerben.<br>Wir beraten Sie gerne! Besuchen Sie uns einfach auf<br><b>www.ralbo-sonderlacke.com</b></p>
  <div class="photo photo-tiles" role="img" aria-label="Badewanne vor bunt gestrichenen Fliesen in Rot, Orange und Grün"><span class="strip"></span></div>
</body>
</html>
```